Simple, Professional and neat business card design for Vendralo Inc.

We're looking to re-vamp our business card design. We're a supplier of innovative feed ingredients for the North American animal agriculture industry. We are located in Lucknow, Ontario, Canada and our flagship product is a product that prevents milk fever in dairy cows when the calve, it is fed before calving and is very effective compared to other alternatives available on the market today.

Our company has Danish roots and we import all of our product from our Danish partner/manufacturer in Denmark. We like our design to embrace high professionalism while remaining neat and simple.

Target Market(s)

B2B, Feed Mills, Veterinary Clinics, Large integrators/producers,

Industry/Entity Type

Agribusiness

Contact Information for Business Card

We like the rounded corners because they make the card easy to sit in a wallet and not many use it so it makes the card stand out, just possibly something to take account for during the design.

As you can also see on the sliders below, looking for a that simple but proffesional scandinavian design.

Requirements
Nice to have
• Rounded corners
Should not have
• Too vibrant

```html
<!DOCTYPE html>
<html lang="en">
<head>
<meta charset="utf-8">
<title>Vendralo Inc. — Business Card</title>
<link href="https://fonts.googleapis.com/css2?family=Lato:wght@900&family=Mulish:wght@600;700&display=swap" rel="stylesheet">
<style>
  :root {
    --backdrop: #b3b3b3;
    --navy: #23529b;
    --cream: #eddab0;
    --bronze: #756c55;
    --sky: #2f63b0;
  }
  * { margin: 0; padding: 0; box-sizing: border-box; }
  html, body { width: 1200px; height: 1200px; overflow: hidden; background: var(--backdrop); }
  .sheet { position: relative; width: 1200px; height: 1200px; }

  .card {
    position: absolute; left: 180px; width: 840px; height: 480px;
    border-radius: 48px; overflow: hidden;
    font-family: "Mulish", sans-serif;
  }
  .card--front { top: 83px; }
  .card--back { top: 636px; }
  .card__bg { position: absolute; inset: 0; width: 840px; height: 480px; display: block; }

  /* front */
  .brand-mark {
    position: absolute; left: 54px; top: 108px; width: 122px; height: 122px;
    border-radius: 50%; background: var(--navy);
  }
  .brand-name {
    position: absolute; left: 220px; top: 126px;
    font-family: "Lato", sans-serif; font-weight: 900;
    font-size: 82px; line-height: 1; letter-spacing: -2px;
    color: var(--navy); white-space: nowrap;
  }
  .social { position: absolute; left: 48px; top: 384px; display: flex; gap: 14px; }
  .social__dot { width: 48px; height: 48px; border-radius: 50%; background: var(--navy); }

  .person {
    position: absolute; right: 48px; top: 308px; text-align: right;
    color: var(--cream); font-weight: 600;
  }
  .person__name { font-size: 36px; line-height: 42px; }
  .person__line { font-size: 28px; line-height: 36px; }

  /* back */
  .contacts {
    position: absolute; right: 48px; top: 92px; list-style: none;
    color: var(--cream); font-weight: 700; font-size: 33px;
  }
  .contacts__item {
    display: flex; justify-content: flex-end; align-items: center;
    height: 66px; gap: 20px;
  }
  .contacts__icon { width: 40px; height: 40px; flex: none; }
  .divider {
    position: absolute; left: 48px; top: 380px; width: 744px; height: 3px;
    background: var(--cream);
  }
  .address {
    position: absolute; left: 48px; top: 398px; width: 744px; text-align: center;
    color: var(--cream); font-weight: 700; font-size: 33px; line-height: 40px;
  }
</style>
</head>
<body>
<main class="sheet">

  <section class="card card--front">
    <svg class="card__bg" viewBox="0 0 840 480" aria-hidden="true">
      <defs>
        <linearGradient id="name-band" x1="280" y1="0" x2="840" y2="0" gradientUnits="userSpaceOnUse">
          <stop offset="0" stop-color="#eddab0"/>
          <stop offset="0.55" stop-color="#a39679"/>
          <stop offset="0.75" stop-color="#756c55"/>
          <stop offset="1" stop-color="#756c55"/>
        </linearGradient>
      </defs>
      <rect width="840" height="480" fill="#23529b"/>
      <path d="M228 0 H840 V480 H0 V237 A228 237 0 0 1 228 0 Z" fill="#eddab0"/>
      <rect x="280" y="288" width="560" height="192" fill="url(#name-band)"/>
    </svg>
    <div class="brand-mark" aria-hidden="true"></div>
    <h1 class="brand-name">VENDRALO INC.</h1>
    <div class="social" aria-label="Social channels">
      <span class="social__dot"></span>
      <span class="social__dot"></span>
      <span class="social__dot"></span>
    </div>
    <div class="person">
      <p class="person__name">Mikkel Sørvang</p>
      <p class="person__line">mikkel@vendralo.com</p>
      <p class="person__line">www.vendralo.com</p>
    </div>
  </section>

  <section class="card card--back">
    <svg class="card__bg" viewBox="0 0 840 480" aria-hidden="true">
      <rect width="840" height="480" fill="#eddab0"/>
      <path d="M224 0 H840 V480 H0 V236 A224 236 0 0 1 224 0 Z" fill="#23529b"/>
    </svg>
    <ul class="contacts">
      <li class="contacts__item">
        <svg class="contacts__icon" viewBox="0 0 40 40" aria-hidden="true">
          <rect x="10" y="2" width="20" height="36" rx="3" fill="none" stroke="#eddab0" stroke-width="3"/>
          <circle cx="20" cy="32" r="2" fill="#eddab0"/>
        </svg>
        <span>Mobile:555-214-0381</span>
      </li>
      <li class="contacts__item">
        <svg class="contacts__icon" viewBox="0 0 40 40" aria-hidden="true">
          <rect x="14" y="6" width="12" height="8" rx="2" fill="none" stroke="#eddab0" stroke-width="3"/>
          <rect x="1" y="12" width="38" height="24" rx="3" fill="#eddab0"/>
        </svg>
        <span>Office:555-309-4716</span>
      </li>
      <li class="contacts__item">
        <svg class="contacts__icon" viewBox="0 0 40 40" aria-hidden="true">
          <circle cx="20" cy="20" r="19" fill="#eddab0"/>
          <path d="M13 10 l5 0 l2 6 l-3 2 q2 5 6 7 l2 -3 l6 2 l0 5 q-2 3 -6 2 q-11 -4 -14 -15 q0 -4 2 -6 Z" fill="#23529b"/>
        </svg>
        <span>Toll Free:800-555-0192</span>
      </li>
      <li class="contacts__item">
        <svg class="contacts__icon" viewBox="0 0 40 40" aria-hidden="true">
          <rect x="1" y="14" width="8" height="24" rx="3" fill="#eddab0"/>
          <rect x="15" y="2" width="16" height="14" fill="none" stroke="#eddab0" stroke-width="2.5"/>
          <rect x="11" y="16" width="28" height="22" rx="2" fill="#eddab0"/>
          <rect x="16" y="22" width="14" height="3" fill="#23529b"/>
        </svg>
        <span>Fax:555-309-4790</span>
      </li>
    </ul>
    <div class="divider" aria-hidden="true"></div>
    <p class="address">Box 412, Fernmoor, Ontario Canada K0L 3T0</p>
  </section>

</main>
</body>
</html>
```